2018 Brontor 3400 Velto construction

Eye catching and progressional design needed, not too busy, must integrate website, phone and our logo. We would like a complete wrap design covering the entire truck. I have a 2018 brontor 3400 crew cab. I am open to designs. Really want people to notice the company vehicle and remember the name and logo.

Target Market(s)

Middle class-to- high end clients

Industry/Entity Type

Construction

Font styles to use
Other font styles liked:
• Montserrat

Colors

Designer to choose colors to be used in the design.

Requirements
Must have
• Phone number: 555-417-2868 Website: Veltoconstruction.example Licensed and insured
Nice to have
• Bathrooms, kitchens, additions, new construction, remodeling

```html
<!DOCTYPE html>
<html lang="en">
<head>
<meta charset="utf-8">
<title>Velto Construction – Truck Wrap Layout</title>
<link rel="stylesheet" href="https://fonts.googleapis.com/css2?family=Montserrat:ital,wght@0,400;0,500;0,700;1,400;1,600&display=swap">
<style>
  :root {
    --page: #ffffff;
    --wrap-black: #161616;
    --wrap-grey: #5c5a58;
    --wrap-grey-dark: #3b3a39;
    --copper: #c99a79;
    --ink-light: #eeeeee;
    --badge-blue: #1f5e97;
    --badge-ink: #ffffff;
  }
  * { margin: 0; padding: 0; box-sizing: border-box; }
  html, body {
    width: 1200px;
    height: 2438px;
    overflow: hidden;
    background: var(--page);
    font-family: "Montserrat", Arial, sans-serif;
  }
  .wrap-sheet { position: relative; width: 1200px; height: 2438px; }
  .panel { position: absolute; display: block; }
  .panel--hood { left: 170px; top: 90px; width: 860px; height: 560px; }
  .panel--driver { left: 20px; top: 860px; width: 1160px; height: 330px; }
  .panel--passenger { left: 20px; top: 1300px; width: 1160px; height: 330px; }
  .panel--tailgate { left: 210px; top: 1860px; width: 780px; height: 330px; }

  .base { fill: var(--wrap-black); }
  .field-grey { fill: var(--wrap-grey); }
  .field-dark { fill: var(--wrap-grey-dark); }
  .stripe-copper { fill: none; stroke: var(--copper); stroke-linecap: round; }
  .logo-square { fill: none; stroke: var(--copper); stroke-width: 2.5; }
  .brand-name { fill: var(--ink-light); font-weight: 500; letter-spacing: 0.2em; }
  .service { fill: var(--ink-light); font-style: italic; font-weight: 400; }
  .bullet { fill: var(--copper); }
  .phone { fill: var(--copper); font-weight: 700; letter-spacing: 0.04em; }
  .web { fill: var(--copper); font-weight: 600; font-style: italic; }
  .badge-plain { fill: var(--badge-blue); }
  .badge-text { fill: var(--badge-ink); font-weight: 700; letter-spacing: 0.04em; }
  .badge-join { fill: var(--badge-ink); font-weight: 500; }
  .hood-name { fill: #6c6a68; font-weight: 500; letter-spacing: 0.25em; }
  .make-name { fill: #c8c8c8; font-weight: 700; letter-spacing: 0.12em; }
  .make-ring { fill: none; stroke: #c8c8c8; stroke-width: 2; }
  .drive-mark { fill: #8a8886; font-weight: 700; letter-spacing: 0.06em; }
</style>
</head>
<body>
<main class="wrap-sheet">

  <!-- Hood -->
  <svg class="panel panel--hood" viewBox="0 0 860 560" aria-label="Hood wrap panel">
    <path class="base" d="M60 0 H800 L860 560 H0 Z"/>
    <path class="field-grey" d="M0 560 L30 300 C260 230 600 230 830 290 L860 560 Z"/>
    <path class="stripe-copper" stroke-width="7" d="M40 300 C270 225 590 225 825 285"/>
    <rect class="logo-square" x="240" y="330" width="60" height="60" stroke-opacity="0.5"/>
    <text class="hood-name" x="320" y="360" font-size="26">VELTO</text>
    <text class="hood-name" x="320" y="396" font-size="26">CONSTRUCTION</text>
  </svg>

  <!-- Driver side -->
  <svg class="panel panel--driver" viewBox="0 0 1160 330" aria-label="Driver side wrap panel">
    <rect class="base" x="0" y="0" width="1160" height="330" rx="14"/>
    <path class="field-grey" d="M850 0 H1146 Q1160 0 1160 14 V316 Q1160 330 1146 330 H770 C790 220 810 110 850 0 Z"/>
    <path class="field-dark" d="M500 330 C640 300 740 230 800 130 C785 200 775 270 770 330 Z"/>
    <path class="stripe-copper" stroke-width="10" d="M885 0 C840 160 720 280 520 322"/>

    <rect class="logo-square" x="350" y="120" width="82" height="82"/>
    <text class="brand-name" x="455" y="150" font-size="26">VELTO</text>
    <text class="brand-name" x="455" y="186" font-size="26">CONSTRUCTION</text>
    <text class="brand-name" x="455" y="214" font-size="17">AND REMODELING</text>

    <g class="badge" transform="rotate(-12 650 60)">
      <rect class="badge-plain" x="600" y="36" width="100" height="48" rx="4"/>
      <text class="badge-text" x="650" y="53" font-size="11" text-anchor="middle">LICENSED</text>
      <text class="badge-join" x="650" y="63" font-size="7" text-anchor="middle">AND</text>
      <text class="badge-text" x="650" y="76" font-size="11" text-anchor="middle">INSURED</text>
    </g>

    <rect class="bullet" x="340" y="254" width="5" height="5"/>
    <text class="service" x="350" y="260" font-size="14">Bathrooms</text>
    <rect class="bullet" x="340" y="274" width="5" height="5"/>
    <text class="service" x="350" y="280" font-size="14">kitchens</text>
    <rect class="bullet" x="436" y="254" width="5" height="5"/>
    <text class="service" x="446" y="260" font-size="14">additions</text>
    <rect class="bullet" x="436" y="274" width="5" height="5"/>
    <text class="service" x="446" y="280" font-size="14">new construction</text>
    <rect class="bullet" x="575" y="265" width="5" height="5"/>
    <text class="service" x="585" y="271" font-size="14">remodeling</text>

    <text class="phone" x="1135" y="56" font-size="32" text-anchor="end">555-417-2868</text>
    <text class="web" x="1135" y="80" font-size="13.5" text-anchor="end">www.Veltoconstruction.example</text>
  </svg>

  <!-- Passenger side -->
  <svg class="panel panel--passenger" viewBox="0 0 1160 330" aria-label="Passenger side wrap panel">
    <g transform="translate(1160 0) scale(-1 1)">
      <rect class="base" x="0" y="0" width="1160" height="330" rx="14"/>
      <path class="field-grey" d="M850 0 H1146 Q1160 0 1160 14 V316 Q1160 330 1146 330 H770 C790 220 810 110 850 0 Z"/>
      <path class="field-dark" d="M500 330 C640 300 740 230 800 130 C785 200 775 270 770 330 Z"/>
      <path class="stripe-copper" stroke-width="10" d="M885 0 C840 160 720 280 520 322"/>
    </g>

    <rect class="logo-square" x="480" y="120" width="82" height="82"/>
    <text class="brand-name" x="585" y="150" font-size="26">VELTO</text>
    <text class="brand-name" x="585" y="186" font-size="26">CONSTRUCTION</text>
    <text class="brand-name" x="585" y="214" font-size="17">AND REMODELING</text>

    <g class="badge" transform="rotate(-12 800 60)">
      <rect class="badge-plain" x="750" y="36" width="100" height="48" rx="4"/>
      <text class="badge-text" x="800" y="53" font-size="11" text-anchor="middle">LICENSED</text>
      <text class="badge-join" x="800" y="63" font-size="7" text-anchor="middle">AND</text>
      <text class="badge-text" x="800" y="76" font-size="11" text-anchor="middle">INSURED</text>
    </g>

    <rect class="bullet" x="590" y="254" width="5" height="5"/>
    <text class="service" x="600" y="260" font-size="14">Bathrooms</text>
    <rect class="bullet" x="590" y="274" width="5" height="5"/>
    <text class="service" x="600" y="280" font-size="14">kitchens</text>
    <rect class="bullet" x="686" y="254" width="5" height="5"/>
    <text class="service" x="696" y="260" font-size="14">additions</text>
    <rect class="bullet" x="686" y="274" width="5" height="5"/>
    <text class="service" x="696" y="280" font-size="14">new construction</text>
    <rect class="bullet" x="828" y="265" width="5" height="5"/>
    <text class="service" x="838" y="271" font-size="14">remodeling</text>

    <text class="phone" x="25" y="56" font-size="32">555-417-2868</text>
    <text class="web" x="25" y="80" font-size="13.5">www.Veltoconstruction.example</text>
  </svg>

  <!-- Tailgate -->
  <svg class="panel panel--tailgate" viewBox="0 0 780 330" aria-label="Tailgate wrap panel">
    <rect class="field-grey" x="0" y="0" width="780" height="330" rx="12"/>
    <path class="base" d="M12 0 H470 C445 150 400 270 330 330 H12 Q0 330 0 318 V12 Q0 0 12 0 Z"/>
    <path class="field-dark" d="M330 330 C400 270 440 200 460 120 C470 210 420 290 400 330 Z"/>
    <path class="stripe-copper" stroke-width="8" d="M478 0 C455 160 410 270 340 326"/>

    <rect class="logo-square" x="24" y="34" width="66" height="66"/>
    <text class="brand-name" x="106" y="58" font-size="19">VELTO</text>
    <text class="brand-name" x="106" y="86" font-size="19">CONSTRUCTION</text>
    <text class="brand-name" x="106" y="106" font-size="13">AND REMODELING</text>

    <rect class="bullet" x="24" y="146" width="6" height="6"/>
    <text class="service" x="36" y="154" font-size="19">Bathrooms</text>
    <rect class="bullet" x="24" y="172" width="6" height="6"/>
    <text class="service" x="36" y="180" font-size="19">kitchens</text>
    <rect class="bullet" x="24" y="198" width="6" height="6"/>
    <text class="service" x="36" y="206" font-size="19">additions</text>
    <rect class="bullet" x="24" y="224" width="6" height="6"/>
    <text class="service" x="36" y="232" font-size="19">new construction</text>
    <rect class="bullet" x="24" y="250" width="6" height="6"/>
    <text class="service" x="36" y="258" font-size="19">remodeling</text>

    <circle class="make-ring" cx="380" cy="100" r="28"/>
    <text class="make-name" x="380" y="148" font-size="13" text-anchor="middle">BRONTOR</text>

    <g class="badge" transform="rotate(-10 590 88)">
      <rect class="badge-plain" x="510" y="54" width="160" height="70" rx="6"/>
      <text class="badge-text" x="590" y="80" font-size="18" text-anchor="middle">LICENSED</text>
      <text class="badge-join" x="590" y="94" font-size="10" text-anchor="middle">AND</text>
      <text class="badge-text" x="590" y="114" font-size="18" text-anchor="middle">INSURED</text>
    </g>
    <text class="drive-mark" x="640" y="176" font-size="24">4X4</text>

    <text class="phone" x="600" y="224" font-size="36" text-anchor="middle">555-417-2868</text>
    <text class="web" x="600" y="254" font-size="17" text-anchor="middle">www.Veltoconstruction.example</text>
  </svg>

</main>
</body>
</html>
```